"Quiet Hollow Fern Taxidermy" is the name of business.

Birds and Small Mammals are the focus. Coyotes, Foxes, Beavers, Ducks, Birds etc.,
Nassology
Preserving the natural beauty of animals through quiet hollow fern.

I would like the logo to include a style of images/symbols in this tattoo and of this buzzard drawing. Not quite hieroglyphic but similar style. Preferred vertically arranged

Art
After on one side
Death
Taxidermy

Snake
Moon on other side
Buzzard

```html
<!DOCTYPE html>
<html lang="en">
<head>
<meta charset="utf-8">
<title>Quiet Hollow Fern Taxidermy — Business Card</title>
<link rel="stylesheet" href="https://fonts.googleapis.com/css2?family=Cinzel:wght@600;700&display=swap">
<style>
  :root {
    --backdrop: #676767;
    --card: #ffffff;
    --bronze: #b0874c;
  }
  * { margin: 0; padding: 0; box-sizing: border-box; }
  html, body { width: 1200px; height: 1200px; overflow: hidden; }
  body { background: var(--backdrop); position: relative; font-family: "Cinzel", serif; color: var(--bronze); }

  .card {
    position: absolute;
    top: 174px;
    width: 472px;
    height: 850px;
    background: var(--card);
  }
  .card--front { left: 94px; }
  .card--back { left: 634px; }

  .brand-mark {
    position: absolute;
    left: 176px;
    top: 293px;
    width: 120px;
    height: 120px;
    border: 3px solid var(--bronze);
    border-radius: 50%;
  }
  .brand-name {
    position: absolute;
    left: 0; right: 0;
    text-align: center;
    font-weight: 700;
    color: var(--bronze);
  }
  .brand-name__title { top: 502px; font-size: 27px; letter-spacing: 0.02em; }
  .brand-name__trade {
    top: 562px;
    font-size: 13px;
    letter-spacing: 0.9em;
    display: flex;
    justify-content: center;
    align-items: center;
    gap: 6px;
  }
  .brand-name__trade::before,
  .brand-name__trade::after {
    content: "";
    width: 5px;
    height: 5px;
    background: var(--bronze);
    transform: rotate(45deg);
  }
  .brand-name__trade::before { margin-right: 12px; }

  .frame { position: absolute; left: 0; top: 0; width: 472px; height: 850px; }

  .back-text {
    position: absolute;
    left: 0; right: 0;
    text-align: center;
    font-weight: 700;
  }
  .specialty { top: 254px; font-size: 22px; line-height: 30px; padding: 0 60px; }
  .person { top: 419px; font-size: 27px; }
  .city { top: 529px; font-size: 27px; }
  .phone { top: 575px; font-size: 30px; letter-spacing: 0.01em; }

  .divider {
    position: absolute;
    left: 174px;
    width: 124px;
    height: 20px;
  }
  .divider--upper { top: 378px; }
  .divider--lower { top: 470px; }
</style>
</head>
<body>
  <section class="card card--front">
    <div class="brand-mark"></div>
    <p class="brand-name brand-name__title">Quiet Hollow Fern</p>
    <p class="brand-name brand-name__trade">TAXIDERMY</p>
  </section>

  <section class="card card--back">
    <svg class="frame" viewBox="0 0 472 850" aria-hidden="true">
      <path d="M68 40 H427 A29 29 0 0 0 456 69 V781 A29 29 0 0 0 427 810 H68 A29 29 0 0 0 39 781 V69 A29 29 0 0 0 68 40 Z"
            fill="none" stroke="var(--bronze)" stroke-width="2.5"/>
    </svg>

    <p class="back-text specialty">Specializing in birds, waterfowl and small mammals</p>

    <svg class="divider divider--upper" viewBox="0 0 124 20" aria-hidden="true">
      <line x1="0" y1="10" x2="40" y2="10" stroke="var(--bronze)" stroke-width="1.6"/>
      <circle cx="62" cy="10" r="6" fill="var(--bronze)"/>
      <line x1="84" y1="10" x2="124" y2="10" stroke="var(--bronze)" stroke-width="1.6"/>
    </svg>

    <p class="back-text person">Rowan Pell</p>

    <svg class="divider divider--lower" viewBox="0 0 124 20" aria-hidden="true">
      <line x1="0" y1="10" x2="40" y2="10" stroke="var(--bronze)" stroke-width="1.6"/>
      <circle cx="62" cy="10" r="6" fill="var(--bronze)"/>
      <line x1="84" y1="10" x2="124" y2="10" stroke="var(--bronze)" stroke-width="1.6"/>
    </svg>

    <p class="back-text city">Ferrow Bend, SC</p>
    <p class="back-text phone">803-555-0147</p>
  </section>
</body>
</html>
```